Business Card Design

We are looking for a double sided business card.

On one side would be our logo

On the Other Side

Martin Kolby
Sales and Marketing

Phone/Text Logo and 530-418-2763
Email Logo and info@plumvalepets.com
Website Logo and www.plumvalepets.com
Facebook Logo and plumvale pets
Instagram Logo and plumvale_pets

Target Market(s)

Pet owners

Contact Information for Business Card

In project description

Requirements
Must have
• Logo

```html
<!DOCTYPE html>
<html lang="en">
<head>
<meta charset="utf-8">
<title>Plumvale Pets – Business Card</title>
<link rel="stylesheet" href="https://fonts.googleapis.com/css2?family=Montserrat:wght@400;500;700;800&display=swap">
<style>
  :root{
    --backdrop:#2a2a2a;
    --card:#141414;
    --silver:#d9d9d9;
    --orange:#f7931e;
    --white:#ffffff;
  }
  html,body{margin:0;padding:0;overflow:hidden;}
  body{
    width:1200px;height:1186px;background:var(--backdrop);
    font-family:"Montserrat",sans-serif;position:relative;
  }
  .card{
    position:absolute;left:180px;width:840px;height:480px;
    background:var(--card);border-radius:28px;overflow:hidden;
    box-shadow:0 10px 30px rgba(0,0,0,.45);
  }
  .card--front{top:73px;}
  .card--back{top:633px;}

  .brand-name{
    font-weight:800;color:var(--silver);text-transform:uppercase;
    letter-spacing:2px;margin:0;line-height:1;white-space:nowrap;
  }
  .brand-dot{
    display:inline-block;border-radius:50%;background:var(--orange);
    vertical-align:middle;
  }

  /* front */
  .front-brand{position:absolute;left:0;right:0;top:160px;text-align:center;}
  .front-brand .brand-name{font-size:72px;}
  .front-brand .brand-dot{width:22px;height:22px;margin-right:16px;}
  .front-url{
    margin-top:34px;color:var(--orange);font-weight:700;font-size:22px;
    letter-spacing:7px;text-transform:uppercase;
  }

  /* back */
  .back-brand{position:absolute;left:64px;top:54px;}
  .back-brand .brand-name{font-size:52px;}
  .back-brand .brand-dot{width:18px;height:18px;margin-left:14px;}

  .contact{position:absolute;left:64px;top:170px;}
  .person{border-left:8px solid var(--orange);padding-left:22px;}
  .person-name{
    margin:0;color:var(--orange);font-weight:700;font-size:36px;line-height:1.1;
  }
  .person-role{margin:4px 0 0;color:var(--white);font-weight:500;font-size:19px;}
  .details{list-style:none;margin:24px 0 0;padding:0 0 0 30px;}
  .details li{
    display:flex;align-items:center;gap:14px;color:var(--white);
    font-size:19px;font-weight:400;height:32px;
  }
  .details svg{width:18px;height:18px;flex:none;}
  .social-dot{width:14px;height:14px;border-radius:50%;background:var(--orange);margin:0 2px;flex:none;}
</style>
</head>
<body>

<section class="card card--front" aria-label="Card front">
  <div class="front-brand">
    <p class="brand-name"><span class="brand-dot"></span>Plumvale Pets</p>
    <div class="front-url">www.plumvalepets.com</div>
  </div>
</section>

<section class="card card--back" aria-label="Card back">
  <div class="back-brand">
    <p class="brand-name">Plumvale Pets<span class="brand-dot"></span></p>
  </div>

  <div class="contact">
    <div class="person">
      <h1 class="person-name">Martin Kolby</h1>
      <p class="person-role">Sales and Marketing</p>
    </div>
    <ul class="details">
      <li>
        <svg viewBox="0 0 24 24" aria-hidden="true"><path fill="#f7931e" d="M6.6 10.8a15 15 0 0 0 6.6 6.6l2.2-2.2c.3-.3.7-.4 1-.2 1.1.4 2.3.6 3.6.6.6 0 1 .4 1 1V20c0 .6-.4 1-1 1A17 17 0 0 1 3 4c0-.6.4-1 1-1h3.5c.6 0 1 .4 1 1 0 1.3.2 2.5.6 3.6.1.3 0 .7-.2 1z"/></svg>
        530-418-2763
      </li>
      <li>
        <svg viewBox="0 0 24 24" aria-hidden="true"><path fill="#f7931e" d="M2 5h20v14H2z"/><path fill="none" stroke="#141414" stroke-width="2" d="M2 6l10 7 10-7"/></svg>
        info@plumvalepets.com
      </li>
      <li>
        <svg viewBox="0 0 24 24" aria-hidden="true"><circle cx="12" cy="12" r="10" fill="none" stroke="#f7931e" stroke-width="2"/><path fill="none" stroke="#f7931e" stroke-width="2" d="M2 12h20M12 2c3 3 3 17 0 20M12 2c-3 3-3 17 0 20"/></svg>
        www.plumvalepets.com
      </li>
      <li><span class="social-dot"></span>@plumvale pets</li>
      <li><span class="social-dot"></span>@plumvale_pets</li>
    </ul>
  </div>
</section>

</body>
</html>
```